Wordpress template re-design of current website

We need a WordPress template design and new look for our existing website. Our existing site it located at www.velmoro.com.au We are a tech company and want a fresh, clean modern website that matches our brand, services and logo colors. Our main Services are hospitality solutions, Velmoro TV solution and managed networks, more information on these can come from our existing website.

Target Market(s)

We are a tech company so must have a modern feel for new technology

Industry/Entity Type

It Company

Number of Pages Required

5+ page

Font styles to use
Sans Serif

Requirements
Must have
• Be based on a wordpress templete design and match the services that we have in our existing website, in the testimonials want a place for video testimonials as well as text. Nice clean icons used for graphics to represent services.
Nice to have
• nice visual representation of our services in the way of clean icons etc
Should not have
• Clutter

```html
<!DOCTYPE html>
<html lang="en">
<head>
<meta charset="utf-8">
<title>Velmoro — Hospitality Solutions</title>
<link rel="stylesheet" href="https://fonts.googleapis.com/css2?family=Roboto:wght@400;500;700&family=Source+Sans+3:wght@400;600&family=Noto+Serif:ital@1&display=swap">
<style>
:root{
  --brand-blue:#0b3f86;
  --slate:#6c7c88;
  --slate-dark:#5d6c77;
  --nav:#76838e;
  --card:#e7e7e7;
  --card-text:#6a7883;
  --body-text:#5e6a73;
  --white:#ffffff;
  --rule:#3d4a54;
}
*{box-sizing:border-box;margin:0;padding:0}
html,body{width:833px;height:1200px;overflow:hidden;background:var(--white)}
body{position:relative;font-family:"Source Sans 3",Arial,sans-serif;color:var(--body-text)}
.abs{position:absolute}
.heading{font-family:"Roboto",Arial,sans-serif;font-weight:500;text-transform:uppercase}

/* header */
.site-header{left:0;top:0;width:833px;height:80px;background:var(--white)}
.brand{left:51px;top:22px;display:flex;align-items:center;gap:8px;font-family:"Roboto",sans-serif;font-weight:700;font-size:28px;color:var(--brand-blue)}
.brand-dot{width:14px;height:14px;border-radius:50%;background:var(--brand-blue)}
.header-phone{left:581px;top:31px;display:flex;align-items:center;gap:6px;font-family:"Roboto",sans-serif;font-size:13px;color:var(--slate-dark)}
.portal-btn{left:696px;top:26px;width:86px;height:27px;border-radius:14px;background:var(--brand-blue);color:var(--white);font-family:"Roboto",sans-serif;font-weight:500;font-size:11px;display:flex;align-items:center;justify-content:center}

/* nav */
.main-nav{left:0;top:80px;width:833px;height:35px;background:var(--nav)}
.nav-item{top:11px;font-family:"Roboto",sans-serif;font-weight:500;font-size:11px;color:var(--white)}
.nav-item.is-active{top:7px;left:143px;width:82px;height:20px;border-radius:5px;background:var(--brand-blue);display:flex;align-items:center;justify-content:center}
.search{left:597px;top:6px;width:185px;height:22px;border-radius:11px;background:var(--white);display:flex;align-items:center;gap:6px;padding-left:9px;font-size:10px;font-style:italic;color:#9aa3aa}

/* hero */
.hero-photo{left:0;top:115px;width:833px;height:160px;background:linear-gradient(90deg,#3f4a35 0%,#6d7566 30%,#a9aba5 55%,#8d8b78 75%,#4b5a36 100%)}
.hero-title{left:51px;top:184px;font-family:"Roboto",sans-serif;font-weight:700;font-size:20px;color:var(--white)}

/* intro */
.intro{left:0;top:275px;width:833px;height:238px;background:var(--slate);box-shadow:inset 0 6px 6px -4px rgba(0,0,0,.35)}
.intro h1{position:absolute;left:51px;top:26px;font-family:"Roboto",sans-serif;font-weight:700;font-size:20.5px;color:var(--white)}
.intro p{position:absolute;left:52px;width:735px;font-size:11.6px;line-height:16.7px;color:var(--white)}

/* advantage */
.section-title{left:0;top:559px;width:833px;text-align:center;font-family:"Roboto",sans-serif;font-weight:700;font-size:20px;color:var(--slate)}
.card{top:604px;width:168px;height:166px;border-radius:16px;background:var(--card);text-align:center}
.card svg{position:absolute;left:50%;top:17px;transform:translateX(-50%)}
.card h3{position:absolute;left:0;top:69px;width:100%;font-family:"Roboto",sans-serif;font-weight:500;font-size:13px;line-height:14.5px;color:var(--card-text);text-transform:uppercase}
.card p{position:absolute;left:14px;top:107px;width:140px;font-size:9.6px;line-height:13px;color:var(--card-text)}

/* quote */
.quote-band{left:0;top:803px;width:833px;height:74px;background:var(--brand-blue);box-shadow:inset 0 5px 5px -3px rgba(0,0,0,.45);display:flex;align-items:center;justify-content:center;text-align:center}
.quote-band p{font-family:"Noto Serif",Georgia,serif;font-style:italic;font-size:15.5px;line-height:18px;color:var(--white);width:680px}

/* partners */
.partner{top:930px;height:30px;background:#c9cdd0;border-radius:3px}

/* footer */
.site-footer{left:0;top:995px;width:833px;height:177px;background:var(--slate);box-shadow:inset 0 5px 5px -3px rgba(0,0,0,.45)}
.footer-col{top:30px}
.footer-col h4{font-family:"Roboto",sans-serif;font-weight:700;font-size:11.5px;color:var(--white);margin-bottom:8px}
.footer-col li{list-style:none;font-size:9.4px;line-height:16.8px;color:var(--white)}
.contact-line{display:flex;gap:8px;font-size:9.2px;line-height:12px;color:var(--white);margin-bottom:8px}
.newsletter-text{font-size:9.2px;line-height:16.5px;color:var(--white);width:240px}
.field{left:489px;width:216px;height:25px;border-radius:3px;background:var(--white);display:flex;align-items:center;gap:6px;padding-left:7px;font-size:9.6px;color:#8a949b}
.signup{left:711px;top:93px;width:70px;height:57px;border-radius:4px;background:#8290a0;color:var(--white);font-family:"Roboto",sans-serif;font-weight:500;font-size:11px;text-align:center}
.signup svg{margin:12px auto 2px;display:block}

/* bottom bar */
.copyright{left:51px;top:1181px;font-size:9.2px;color:#7d868d;display:flex;align-items:center;gap:6px}
.social-dot{width:8px;height:8px;border-radius:50%;background:#9aa3aa}
.chat{left:631px;top:1177px;width:150px;height:23px;border-radius:4px 4px 0 0;background:#7e8993;color:var(--white);font-family:"Roboto",sans-serif;font-size:8.5px;display:flex;align-items:center;gap:5px;padding-left:10px}
</style>
</head>
<body>

<header class="site-header abs">
  <div class="brand abs"><span class="brand-dot"></span>Velmoro</div>
  <div class="header-phone abs">
    <svg width="18" height="18" viewBox="0 0 18 18"><circle cx="9" cy="9" r="9" fill="var(--brand-blue)"/><path d="M6 5.2c.5-.4 1-.3 1.3.2l.8 1.3c.2.4.1.8-.2 1l-.5.4c.4.9 1.1 1.6 2 2l.4-.5c.3-.3.7-.4 1-.2l1.3.8c.5.3.6.8.2 1.3l-.5.6c-.5.5-1.3.5-2 .2-2-.9-3.5-2.4-4.4-4.4-.3-.7-.3-1.5.2-2z" fill="#fff"/></svg>
    1300 555 214
  </div>
  <div class="portal-btn abs">PORTAL</div>
</header>

<nav class="main-nav abs">
  <span class="nav-item abs" style="left:77px">HOME</span>
  <span class="nav-item is-active abs">SERVICES</span>
  <span class="nav-item abs" style="left:260px">ABOUT</span>
  <span class="nav-item abs" style="left:347px">OUR WORK</span>
  <span class="nav-item abs" style="left:453px">CONTACT</span>
  <div class="search abs">
    <svg width="10" height="10" viewBox="0 0 10 10"><circle cx="4.2" cy="4.2" r="3.2" fill="none" stroke="#5e6a73" stroke-width="1.3"/><path d="M6.6 6.6L9.2 9.2" stroke="#5e6a73" stroke-width="1.4"/></svg>
    Search
  </div>
</nav>

<div class="hero-photo abs" role="img" aria-label="Photo of a modern hotel building facade with glass balconies and trees"></div>
<div class="hero-title abs">HOSPITALITY SOLUTIONS</div>

<section class="intro abs">
  <h1>GET ON THE FASTEST, MOST FLEXIBLE INTERNET ACCESS SYSTEM</h1>
  <p style="top:60px">Our high quality Wi Fi networks offer a robust 24/7 connectivity, enhancing our client's hospitality services. Whether travelling for business or pleasure, guests like to stay connected with their families, friends, and more importantly, with their work. Velmoro's award-winning gateway devices provide an exceptional, easy-to-use interface that delivers on our exceptional service.</p>
  <p style="top:127px">We back our words with an expert support team. If the system faces any issues highly trained technicians are available on the spot to remedy the problem. Our advanced systems integrate easily with the client's current IT system offering advanced options such as paid access, which can be charged directly to the room account. Another option we provide is payment through credit cards or by vouchers created from our club-based customer portal.</p>
  <p style="top:194px">The sole focus of Velmoro's hospitality solutions is to make them an intuitive, guest friendly experience.</p>
</section>
<svg class="abs" style="left:391px;top:512px" width="52" height="26" viewBox="0 0 52 26"><path d="M0 0H52C38 2 30 10 26 25 22 10 14 2 0 0Z" fill="var(--slate)"/></svg>

<h2 class="section-title abs">THE VELMORO ADVANTAGE</h2>

<div class="card abs" style="left:51px">
  <svg width="38" height="36" viewBox="0 0 38 36"><rect x="1" y="15" width="8" height="19" rx="1" fill="var(--slate)"/><path d="M12 15l7-9c1-3 2-6 4-6 3 0 3 4 2 8h8c3 0 4 3 3 5l-3 15c-.5 2-2 3-4 3H12z" fill="var(--slate)"/></svg>
  <h3>Custom Designed<br>Login Pages</h3>
  <p>We design login pages that reflect our client's brand.</p>
</div>
<div class="card abs" style="left:239px">
  <svg width="26" height="36" viewBox="0 0 26 36"><path d="M0 0h26v36L13 26 0 36z" fill="var(--slate)"/></svg>
  <h3>Complete PMS<br>Intergration</h3>
  <p>Guests can charge their internet access directly to their room account.</p>
</div>
<div class="card abs" style="left:426px">
  <svg width="22" height="36" viewBox="0 0 22 36"><rect x="1" y="1" width="20" height="34" rx="3" fill="none" stroke="var(--slate)" stroke-width="2"/><rect x="4" y="6" width="14" height="22" fill="none" stroke="var(--slate)" stroke-width="1.2"/><circle cx="11" cy="31.5" r="1.5" fill="var(--slate)"/></svg>
  <h3>Easy<br>To Use</h3>
  <p>Our systems are adapted for mobile and tablet use as well.</p>
</div>
<div class="card abs" style="left:614px">
  <svg width="36" height="36" viewBox="0 0 36 36"><circle cx="18" cy="18" r="16" fill="none" stroke="var(--slate)" stroke-width="2.4"/><circle cx="18" cy="18" r="7.5" fill="none" stroke="var(--slate)" stroke-width="2.4"/><path d="M7 7l6 6M29 7l-6 6M7 29l6-6M29 29l-6-6" stroke="var(--slate)" stroke-width="3"/></svg>
  <h3>Full Support<br>Options</h3>
  <p>24/7 monitoring backed by 24/7 support centre</p>
</div>

<div class="quote-band abs">
  <p>Survey after survey lists hi-speed internet access and connectivity as the most important facility necessary to the modern traveller. - Stay Industry Review</p>
</div>
<svg class="abs" style="left:391px;top:876px" width="52" height="26" viewBox="0 0 52 26"><path d="M0 0H52C38 2 30 10 26 25 22 10 14 2 0 0Z" fill="var(--brand-blue)"/></svg>

<div class="partner abs" style="left:126px;width:66px"></div>
<div class="partner abs" style="left:246px;width:74px"></div>
<div class="partner abs" style="left:370px;width:76px"></div>
<div class="partner abs" style="left:505px;top:924px;width:56px;height:42px"></div>
<div class="partner abs" style="left:618px;top:922px;width:80px;height:48px;background:#8e9296"></div>

<footer class="site-footer abs">
  <div class="footer-col abs" style="left:51px">
    <h4>QUICK LINKS</h4>
    <ul><li>Home</li><li>Services</li><li>About</li><li>Our Work</li><li>Contact</li></ul>
  </div>
  <div class="footer-col abs" style="left:175px">
    <h4>USEFUL LINKS</h4>
    <ul><li>Case Studies</li><li>Testimonials</li><li>News</li><li>Resellers</li></ul>
  </div>
  <div class="footer-col abs" style="left:323px">
    <h4>CONTACT US</h4>
    <div class="contact-line"><svg width="8" height="10" viewBox="0 0 8 10"><path d="M4 0a4 4 0 0 1 4 4c0 3-4 6-4 6S0 7 0 4a4 4 0 0 1 4-4z" fill="#9fb0bd"/></svg><span>48 Harbour Lane<br>Coral Bay, QLD 4200</span></div>
    <div class="contact-line" style="margin-top:10px"><svg width="10" height="10" viewBox="0 0 10 10"><path d="M2 1c.4-.3.8-.2 1 .2l.8 1.2c.2.3.1.7-.2.9l-.4.3c.4.8 1 1.4 1.8 1.8l.3-.4c.2-.3.6-.4.9-.2l1.2.8c.4.2.5.6.2 1l-.5.5C6.6 7.5 5.9 7.5 5.3 7.2 3.6 6.4 2.4 5.2 1.6 3.5 1.3 2.9 1.3 2.2 1.8 1.7z" fill="#9fb0bd"/></svg>1300 555 214</div>
    <div class="contact-line"><svg width="10" height="9" viewBox="0 0 10 9"><path d="M0 3l5-3 5 3v6H0z" fill="none" stroke="#9fb0bd" stroke-width="1.2"/></svg>sales@velmoro.com.au</div>
  </div>
  <div class="footer-col abs" style="left:488px">
    <h4>NEWSLETER SIGN UP</h4>
    <p class="newsletter-text">Enter your name and email to subscribe or unsubscribe to receive&nbsp; latest news &amp; offers!!!</p>
  </div>
  <div class="field abs" style="top:93px"><svg width="9" height="10" viewBox="0 0 9 10"><circle cx="4.5" cy="2.6" r="2.4" fill="#6c7c88"/><path d="M0 10c0-3 2-4.5 4.5-4.5S9 7 9 10z" fill="#6c7c88"/></svg>Enter Your Name</div>
  <div class="field abs" style="top:125px"><svg width="10" height="9" viewBox="0 0 10 9"><path d="M0 3l5-3 5 3v6H0z" fill="none" stroke="#6c7c88" stroke-width="1.2"/></svg>Enter Your Email</div>
  <div class="signup abs">
    <svg width="22" height="20" viewBox="0 0 22 20"><path d="M22 0L0 9l7 2 2 8 4-5 5 3z" fill="#fff"/></svg>
    SIGN UP
  </div>
</footer>

<div class="copyright abs">© Copyright 2015 Velmoro Wireless Internet All Rights Reserved. <span class="social-dot"></span><span class="social-dot"></span></div>
<div class="chat abs">
  <svg width="14" height="11" viewBox="0 0 14 11"><ellipse cx="7" cy="4.5" rx="7" ry="4.5" fill="#4d5963"/><path d="M3 8l-1 3 4-2z" fill="#4d5963"/></svg>
  Live Chat Offline
  <span style="margin-left:auto;display:flex;gap:4px;padding-right:8px"><span class="social-dot" style="background:#c8ced3;width:10px;height:10px"></span><span class="social-dot" style="background:#c8ced3;width:10px;height:10px"></span></span>
</div>

</body>
</html>
```